Lantern - Web Design Project

We are seeking to have our website redesigned. Our current webpage is rather dated looking www.lantern-outcomes.com We will be utilizing similar content to explain our services as what is in the website now. We do not see it at a retail portal but rather a website for those inquiring about our services as a reference check so to speak.

We wish to have a look that is considered clean, fresh, contemporary and contains a business savvy vibe.

We prefer isolated white background and also wish to retain the integrity of our Logo and colour scheme.

We are looking for something that doesnt look like it was designed at home on sitemoose. We are hoping to find something that looks like it would reside on a tablet.
Updates

Hello designers!

We apologize for our tardiness as we have been quite preoccupied. We will be extending our invites to the end of January!

Hello All,

Please review our offer once again for updated requirements.  We are hoping to accept a design by months end.

Lantern

Target Market(s)

Business to business clients and Large manufacturers

Industry/Entity Type

Retail

Requirements
Must have
• Existing Logo

There must be an area dedicated to an intro video that will be incorporated on our landing page.

We require design of the other pages as well not only the landing page.

```html
<!DOCTYPE html>
<html lang="en">
<head>
<meta charset="utf-8">
<title>Lantern Performance Group</title>
<link href="https://fonts.googleapis.com/css2?family=Questrial&family=Cinzel:wght@400&family=Montserrat:wght@600&display=swap" rel="stylesheet">
<style>
  :root {
    --red: #e3161d;
    --ink: #222222;
    --text: #2b2b2b;
    --muted: #555555;
    --rule: #dcdcdc;
    --bg-grey: #e9e9e9;
    --white: #ffffff;
    --video-dark: rgba(20,20,24,.72);
  }
  * { margin: 0; padding: 0; box-sizing: border-box; }
  html, body { width: 1200px; height: 1078px; overflow: hidden; }
  body {
    position: relative;
    background: var(--white);
    font-family: "Questrial", "Century Gothic", sans-serif;
    color: var(--text);
  }
  .page-top {
    position: absolute; left: 0; top: 0; width: 1200px; height: 496px;
    background: radial-gradient(ellipse 700px 400px at 600px 120px, #ffffff 0%, #f3f3f3 55%, var(--bg-grey) 100%);
  }
  .top-rule { position: absolute; left: 140px; top: 0; width: 920px; height: 3px; background: var(--red); }
  .brand {
    position: absolute; left: 140px; top: 34px;
    display: flex; align-items: center; gap: 10px;
    font-size: 46px; color: #4a4a4a; letter-spacing: -1px;
  }
  .brand-dot { width: 18px; height: 18px; border-radius: 50%; background: var(--red); }
  .utility {
    position: absolute; left: 758px; top: 59px;
    font-size: 11.5px; letter-spacing: .5px; color: #333;
    display: flex; gap: 14px;
  }
  .utility .sep { color: #888; }
  .search {
    position: absolute; left: 919px; top: 56px; width: 141px; height: 20px;
    background: var(--white); border: 1px solid #d4d4d4; border-radius: 2px;
    font-size: 11px; color: #333; padding: 3px 7px;
  }
  .search svg { position: absolute; right: 5px; top: 3px; }
  .main-nav {
    position: absolute; left: 140px; top: 118px; width: 920px; height: 38px;
    background: linear-gradient(#ffffff, #f1f1f1);
    box-shadow: 0 1px 2px rgba(0,0,0,.08);
  }
  .main-nav a {
    position: absolute; top: 12px; font-size: 13px; color: #333; text-decoration: none; letter-spacing: .3px;
  }
  .main-nav .current::after {
    content: ""; position: absolute; left: -20px; right: -20px; top: 24px; height: 2px; background: var(--red);
  }
  .main-nav .current::before {
    content: ""; position: absolute; left: -20px; right: -20px; top: -12px; height: 1px; background: #999;
  }
  .intro-video {
    position: absolute; left: 140px; top: 164px; width: 920px; height: 330px;
    box-shadow: 0 18px 30px -18px rgba(0,0,0,.35);
    overflow: hidden;
  }
  .video-frame {
    position: absolute; inset: 0;
    background: linear-gradient(180deg, #0f3a78 0%, #1a5aa0 35%, #2b3040 62%, #3b2a1c 85%, #1c140c 100%);
  }
  .play-button {
    position: absolute; left: 425px; top: 98px; width: 70px; height: 70px;
    border: 0; background: none; cursor: pointer;
  }
  .video-caption {
    position: absolute; left: 0; bottom: 0; width: 100%; height: 65px;
    background: var(--video-dark);
    font-family: "Cinzel", serif; color: var(--white); font-size: 17px; line-height: 24px;
    padding: 8px 21px;
  }
  .video-arrows {
    position: absolute; left: 855px; top: 230px; width: 40px; height: 21px;
    background: var(--red); border-radius: 10px;
  }
  .side-panel { position: absolute; left: 140px; top: 551px; width: 258px; }
  .side-title {
    height: 37px; border-top: 3px solid var(--red);
    background: linear-gradient(#f9f9f9, #e6e6e6);
    font-size: 17px; color: #333; padding: 8px 12px; letter-spacing: .3px;
  }
  .side-list { list-style: none; margin-top: 5px; }
  .side-list li {
    height: 27.2px; border-bottom: 1px solid #e2e2e2;
    font-size: 13px; color: #222; padding: 5px 0 0 26px; position: relative;
  }
  .side-list li:last-child { border-bottom: none; }
  .side-list li::before {
    content: "»"; position: absolute; left: 11px; top: 4px; color: var(--red); font-size: 12px;
  }
  .welcome { position: absolute; left: 481px; top: 546px; width: 580px; }
  .welcome h1 {
    font-family: "Montserrat", sans-serif; font-weight: 600; font-size: 19px; color: var(--ink);
  }
  .welcome h1 span { color: var(--red); }
  .welcome .dots { margin: 10px 0 0 5px; height: 4px; border-top: 1px dotted #bbb; border-bottom: 1px dotted #bbb; }
  .welcome p { font-size: 14.9px; line-height: 23.5px; color: var(--text); margin-top: 25px; }
  .welcome p + p { margin-top: 23px; }
  .footer {
    position: absolute; left: 0; top: 918px; width: 1200px; height: 160px;
    border-top: 1px solid #d8d8d8;
    background: linear-gradient(#ececec, #ffffff 60%);
    text-align: center; font-size: 11px; color: var(--muted);
  }
  .footer-links { margin-top: 20px; }
  .footer-links span { margin: 0 6px; }
  .footer-contact { margin-top: 17px; }
  .footer-contact b { color: var(--red); font-weight: normal; }
  .footer-copy { margin-top: 16px; }
  .social { display: flex; gap: 6px; justify-content: center; margin-top: 18px; }
  .social i { width: 16px; height: 16px; border-radius: 2px; display: block; }
</style>
</head>
<body>
  <div class="page-top"></div>
  <div class="top-rule"></div>

  <div class="brand"><span class="brand-dot"></span>Lantern</div>

  <div class="utility"><span>SIGN IN</span><span class="sep">|</span><span>FRANÇAIS</span></div>
  <div class="search">Search...
    <svg width="13" height="13" viewBox="0 0 13 13"><circle cx="5.5" cy="5.5" r="4" fill="none" stroke="#555" stroke-width="1.4"/><line x1="8.5" y1="8.5" x2="12" y2="12" stroke="#555" stroke-width="1.6"/></svg>
  </div>

  <nav class="main-nav">
    <a class="current" style="left:42px">HOME</a>
    <a style="left:132px">WHO WE ARE</a>
    <a style="left:268px">CROSS THE LANTERN</a>
    <a style="left:437px">PERFORMANCE SOLUTIONS</a>
    <a style="left:653px">SUSTAIN SOLUTIONS</a>
    <a style="left:830px">JOIN US</a>
  </nav>

  <section class="intro-video" aria-label="Intro video">
    <div class="video-frame" role="img" aria-label="Intro video poster: city skyline at night with light trails of traffic"></div>
    <button class="play-button" aria-label="Play intro video">
      <svg width="70" height="70" viewBox="0 0 70 70"><circle cx="35" cy="35" r="33" fill="rgba(0,0,0,.35)" stroke="#fff" stroke-width="2"/><path d="M28 22 L50 35 L28 48 Z" fill="#fff"/></svg>
    </button>
    <div class="video-arrows">
      <svg width="40" height="21" viewBox="0 0 40 21"><path d="M15 6 L11 10.5 L15 15" fill="none" stroke="#fff" stroke-width="1.6"/><path d="M25 6 L29 10.5 L25 15" fill="none" stroke="#fff" stroke-width="1.6"/></svg>
    </div>
    <div class="video-caption">"Customer satisfaction is worthless, customer loyalty is priceless."<br>- Martin Halvers</div>
  </section>

  <aside class="side-panel">
    <div class="side-title">PERFORMANCE SOLUTIONS</div>
    <ul class="side-list">
      <li>Business Diagnostics</li>
      <li>Executive Coaching</li>
      <li>Management Development</li>
      <li>Talent Management</li>
      <li>Creating Sales Culture</li>
      <li>Creating Customer</li>
      <li>Loyalty Performance</li>
      <li>Improvement Initiatives</li>
      <li>Finance &amp; Insurance</li>
      <li>Training Product Launches</li>
    </ul>
  </aside>

  <main class="welcome">
    <h1>Welcome to <span>Lantern Performance Group</span></h1>
    <div class="dots"></div>
    <p>Lantern Performance Group Inc. is the leading provider of profit generating and people development solutions. With the hands-on experience of best practices, the state-of-the-art technology and in-depth information we help companies increase their efficiencies and profits. Frank, honest, committed, valuable and rewarding are words that customers use to describe the quality services provided by Lantern Performance Group.</p>
    <p>&nbsp;Learn more about us, or find the right solutions for your specific business.We will be delighted to help you achieve better business results.</p>
  </main>

  <footer class="footer">
    <div class="footer-links">Home<span>-</span>Who We Are<span>-</span>Cross The Lantern<span>-</span>Performance Solutions<span>-</span>Sustain Solutions<span>-</span>Join Us<span>-</span>Site Map</div>
    <div class="footer-contact">58 Fernhill Ave, Kingsford, ON K2R 4T8, Canada &nbsp;<b>T</b> :+1.800.555.0142 &nbsp;<b>E</b> :info@lantern-outcomes.com</div>
    <div class="footer-copy">Copyright © 2012 Lantern Performance. All Rights Reserved.</div>
    <div class="social">
      <i style="background:#4a67a8"></i>
      <i style="background:#3a7fb8"></i>
      <i style="background:#4fb6e0"></i>
    </div>
  </footer>
</body>
</html>
```